Website Design for Bright Path Learning

The business is called Bright Path Learning - a Drug & Alcohol Education program for Sydney school kids. I wish to create a simple online business card which covers who we are, the programs we offer and why they should choose us. I would like the business page to be very colourful and school-friendly, but with the seriousness of alcohol and drug use. I have attached some pictures and logos for the business. The programs are called 'clear road' for high school, and 'step ahead' for primary school. The logo is black & white. There is also a photo of the manager with some kids.

```html
<!DOCTYPE html>
<html lang="en">
<head>
<meta charset="utf-8">
<title>Bright Path Learning</title>
<link rel="stylesheet" href="https://fonts.googleapis.com/css2?family=Lilita+One&family=PT+Sans:wght@400;700&family=PT+Sans+Narrow&family=PT+Serif&display=swap">
<style>
:root{
  --paper:#f5f5f3;
  --paper-shade:#e9e9e6;
  --red:#ee5a2c;
  --orange:#f7ae0b;
  --gold:#f0b21a;
  --ink:#222;
  --grey:#666;
  --white:#fff;
  --sky:#c6def0;
  --hero-warm:#f4a27b;
  --hero-grass:#8cc63f;
  --art-bg:#e9a82b;
}
*{margin:0;padding:0;box-sizing:border-box}
html,body{width:1200px;height:1071px;overflow:hidden}
body{
  position:relative;
  background:radial-gradient(ellipse at 40% 30%,var(--white) 0%,var(--paper) 55%,var(--paper-shade) 100%);
  font-family:"PT Sans",sans-serif;color:var(--ink);
}
.abs{position:absolute}
.splash{left:540px;top:85px;width:380px;height:70px;border-radius:50%;
  background:radial-gradient(ellipse,var(--sky) 0%,rgba(198,222,240,0) 70%)}
.brand{left:183px;top:76px;font-family:"Lilita One",sans-serif;font-size:33px;line-height:40px;color:var(--red);letter-spacing:1px;display:flex;align-items:center;gap:12px;white-space:nowrap}
.brand-dot{width:20px;height:20px;border-radius:50%;background:var(--red)}
.main-nav{right:174px;top:82px;display:flex;gap:16px;white-space:nowrap}
.nav{font-family:"Lilita One",sans-serif;font-size:14px;line-height:18px;color:var(--gold);text-transform:uppercase}
.nav.active{color:var(--red)}
.hero{left:178px;top:145px;width:584px;height:267px;background:var(--white);box-shadow:0 1px 4px rgba(0,0,0,.12)}
.hero-art{position:absolute;left:7px;top:8px;width:570px;height:220px;border:3px solid var(--ink);
  background:linear-gradient(180deg,var(--hero-warm) 0%,#f6b890 70%,var(--hero-grass) 88%)}
.pager{position:absolute;right:10px;bottom:10px;font-family:"PT Sans Narrow",sans-serif;font-size:13px;color:var(--gold);letter-spacing:5px}
.program{left:762px;top:145px;width:214px;height:267px;background:var(--white)}
.program h2{font-family:"Lilita One",sans-serif;font-weight:400;font-size:25px;color:var(--red);margin:20px 0 0 22px}
.program .rule{margin:8px 18px 0 22px;border-top:2px dotted #bbb}
.prog-item{margin:16px 0 0 22px}
.prog-item h3{font-weight:400;font-size:16px;color:var(--gold)}
.prog-item p{font-family:"PT Sans Narrow",sans-serif;font-size:11px;margin-top:4px}
.strip{left:976px;top:145px;width:50px;height:267px;border:2px solid var(--gold);border-radius:3px}
.section-title{font-family:"Lilita One",sans-serif;font-weight:400;font-size:19px;color:var(--red);text-transform:uppercase}
.why-text{left:178px;top:476px;width:540px;font-family:"PT Sans Narrow",sans-serif;font-size:12px;line-height:18px}
.read-more{font-family:"Lilita One",sans-serif;font-size:17px;color:var(--gold);display:flex;align-items:center;gap:8px}
.band .read-more{color:var(--red)}
.contact-title{left:765px;top:438px;color:var(--gold)}
.hours-label{left:822px;top:484px;font-family:"PT Serif",serif;font-size:10px;color:var(--grey);text-transform:uppercase}
.hours{left:822px;top:496px;font-family:"PT Serif",serif;font-size:17px}
.contact-rule{left:822px;top:531px;width:204px;border-top:2px dotted #bbb}
.phone-label{left:822px;top:548px;font-family:"PT Serif",serif;font-size:10px;color:var(--grey);text-decoration:underline;text-transform:uppercase}
.phone{left:822px;top:560px;font-family:"PT Sans Narrow",sans-serif;font-size:14px}
.band{left:0;top:614px;width:1200px;height:373px;background:var(--orange)}
.zig{position:absolute;left:0;width:1200px;height:12px}
.col{position:absolute;top:0;width:262px}
.col h2{font-family:"PT Serif",serif;font-weight:400;font-size:20px;color:var(--white);margin-top:31px}
.col .frame{margin-top:24px;height:118px;background:var(--white);padding:6px;box-shadow:0 1px 3px rgba(0,0,0,.15)}
.col .fill{width:100%;height:100%}
.col p{margin-top:10px;font-family:"PT Sans Narrow",sans-serif;font-size:12px;line-height:18px;color:var(--white)}
.col .read-more{margin-top:2px}
.foot-rule{left:120px;top:1016px;width:940px;border-top:2px dashed #aaa}
.copyright{left:178px;top:1036px;font-family:"PT Sans Narrow",sans-serif;font-size:10px;color:var(--grey)}
.foot-links{right:172px;top:1034px;font-family:"PT Serif",serif;font-size:11px;color:var(--ink)}
</style>
</head>
<body>
<div class="abs splash"></div>

<div class="abs brand"><span class="brand-dot"></span>Bright Path Learning</div>
<nav class="abs main-nav">
  <span class="nav active">Home</span>
  <span class="nav">Who we are</span>
  <span class="nav">Program &#187;</span>
  <span class="nav">Why choose us</span>
  <span class="nav">Contact</span>
</nav>

<section class="abs hero">
  <div class="hero-art" role="img" aria-label="Cartoon of two school kids walking past a school, threatened by an alcohol mug, a drug syringe and a violence knife"></div>
  <div class="pager">&#171; 1 2 3 4 5 &#187;</div>
</section>

<aside class="abs program">
  <h2>OUR PROGRAM</h2>
  <div class="rule"></div>
  <div class="prog-item"><h3>Clear Road</h3><p>For high school</p></div>
  <div class="prog-item"><h3>Step Ahead</h3><p>For Primary school</p></div>
  <div class="prog-item"><h3>Drug &amp; Alcohol</h3><p>Program for Sydney school kids.</p></div>
</aside>
<div class="abs strip">
  <svg width="46" height="263" viewBox="0 0 46 263">
    <line x1="0" y1="48" x2="46" y2="48" stroke="#f0b21a" stroke-width="2"/>
    <line x1="0" y1="215" x2="46" y2="215" stroke="#f0b21a" stroke-width="2"/>
    <circle cx="23" cy="24" r="13" fill="none" stroke="#f0b21a" stroke-width="2"/>
    <path d="M17 27l6-6 6 6M17 22l6-6 6 6" fill="none" stroke="#f0b21a" stroke-width="2"/>
    <circle cx="23" cy="238" r="13" fill="none" stroke="#f0b21a" stroke-width="2"/>
    <path d="M17 235l6 6 6-6M17 240l6 6 6-6" fill="none" stroke="#f0b21a" stroke-width="2"/>
  </svg>
</div>

<h2 class="abs section-title" style="left:178px;top:440px">Why choose us ?</h2>
<p class="abs why-text">Each Open Field Schools network school reflects the vision of its leadership and staff,but all schools share a common mission and philosophy.&nbsp; Although we encourage flexibility and innovation at the individual school level, our School Hallmarks and Core Beliefs are at the heart of every one of our schools.</p>
<div class="abs read-more" style="left:178px;top:556px">READ MORE
  <svg width="30" height="30" viewBox="0 0 30 30"><circle cx="15" cy="15" r="13" fill="none" stroke="#f0b21a" stroke-width="2"/><path d="M11 11l4 4-4 4M16 11l4 4-4 4" fill="none" stroke="#f0b21a" stroke-width="2"/></svg>
</div>

<h2 class="abs section-title contact-title">Contact us</h2>
<svg class="abs" style="left:764px;top:480px" width="38" height="38" viewBox="0 0 38 38"><circle cx="19" cy="19" r="16" fill="none" stroke="#f0b21a" stroke-width="2"/><path d="M19 8v11l7 5" fill="none" stroke="#f0b21a" stroke-width="2"/></svg>
<div class="abs hours-label">7 days a week</div>
<div class="abs hours">10:00 am - 1:30 pm</div>
<div class="abs contact-rule"></div>
<svg class="abs" style="left:764px;top:544px" width="40" height="38" viewBox="0 0 40 38"><path d="M4 12c0-5 32-5 32 0v3h-8v-3c-5-2-11-2-16 0v3H4z" fill="none" stroke="#f0b21a" stroke-width="2"/><rect x="8" y="17" width="24" height="16" rx="2" fill="none" stroke="#f0b21a" stroke-width="2"/><circle cx="20" cy="25" r="4" fill="none" stroke="#f0b21a" stroke-width="2"/></svg>
<div class="abs phone-label">Contact phone</div>
<div class="abs phone">+ 000&nbsp; 0000000</div>

<section class="abs band">
  <svg class="zig" style="top:-11px" viewBox="0 0 1200 12" preserveAspectRatio="none"><defs><pattern id="zt" width="12" height="12" patternUnits="userSpaceOnUse"><path d="M0 12L6 0l6 12z" fill="#f7ae0b"/></pattern></defs><rect width="1200" height="12" fill="url(#zt)"/></svg>
  <svg class="zig" style="bottom:-11px" viewBox="0 0 1200 12" preserveAspectRatio="none"><defs><pattern id="zb" width="12" height="12" patternUnits="userSpaceOnUse"><path d="M0 0l6 12 6-12z" fill="#f7ae0b"/></pattern></defs><rect width="1200" height="12" fill="url(#zb)"/></svg>

  <article class="col" style="left:178px">
    <h2>What we do</h2>
    <div class="frame"><div class="fill" role="img" aria-label="Photo of the program manager with a group of kids outdoors" style="background:linear-gradient(90deg,#8a8f94,#c9ccd0 60%,#e6e8ea)"></div></div>
    <p>Each Open Field Schools network school reflects the vision of its leadership and staff,but all schools share a common mission and philosophy.&nbsp; Although we encourage flexibility and innovation at the individual school level, our School Hallmarks and Core Beliefs are at the heart of every one of our schools.</p>
    <div class="read-more">READ MORE <svg width="30" height="30" viewBox="0 0 30 30"><circle cx="15" cy="15" r="13" fill="none" stroke="#ee5a2c" stroke-width="2"/><path d="M11 11l4 4-4 4M16 11l4 4-4 4" fill="none" stroke="#ee5a2c" stroke-width="2"/></svg></div>
  </article>

  <article class="col" style="left:470px">
    <h2>School approach</h2>
    <div class="frame"><div class="fill" role="img" aria-label="Step Ahead program artwork with a book, paintbrush and pencil" style="background:var(--art-bg)"></div></div>
    <p>Each Open Field Schools network school reflects the vision of its leadership and staff,but all schools share a common mission and philosophy.&nbsp; Although we encourage flexibility and innovation at the individual school level, our School Hallmarks and Core Beliefs are at the heart of every one of our schools.</p>
    <div class="read-more">READ MORE <svg width="30" height="30" viewBox="0 0 30 30"><circle cx="15" cy="15" r="13" fill="none" stroke="#ee5a2c" stroke-width="2"/><path d="M11 11l4 4-4 4M16 11l4 4-4 4" fill="none" stroke="#ee5a2c" stroke-width="2"/></svg></div>
  </article>

  <article class="col" style="left:764px">
    <h2>Active learning</h2>
    <div class="frame"><div class="fill" role="img" aria-label="Clear Road program artwork with cigarettes, syringes and pills" style="background:var(--art-bg)"></div></div>
    <p>Each Open Field Schools network school reflects the vision of its leadership and staff,but all schools share a common mission and philosophy.&nbsp; Although we encourage flexibility and innovation at the individual school level, our School Hallmarks and Core Beliefs are at the heart of every one of our schools.</p>
    <div class="read-more">READ MORE <svg width="30" height="30" viewBox="0 0 30 30"><circle cx="15" cy="15" r="13" fill="none" stroke="#ee5a2c" stroke-width="2"/><path d="M11 11l4 4-4 4M16 11l4 4-4 4" fill="none" stroke="#ee5a2c" stroke-width="2"/></svg></div>
  </article>
</section>

<footer>
  <div class="abs foot-rule"></div>
  <div class="abs copyright">&copy; 2014 Lumenfold Studio copyright</div>
  <div class="abs foot-links">Site Map |&nbsp;&nbsp; Copyrights |&nbsp;&nbsp; Terms &amp; Conditions</div>
</footer>
</body>
</html>
```